Brochure for a conference with healthcare professionals

Creating a brochure with the information provided in the word document attached below.. along with the logo.. All the information for the brochure is in the word document.. I attached a logo of endocrinology dept in the files.. Use that logo more promintenly than the brenmore care logo..

Most of the designs submitted till now didn't understand what was written on the word document.. The tri-fold should be designed to tell a story.. it should capture the attention just by its title.. then all the information provided should hook them in..

Target Market(s)

Physicians and CEOs of hospitals

Industry/Entity Type

Healthcare

Font styles to use
Serif

Colors

Designer to choose colors to be used in the design.

Requirements
Must have
• Good and memorable design with pictures and elegant design.. The design I am expecting is a tri-fold 9x16 size that can be tested on quellorint.example..

```html
<!DOCTYPE html>
<html lang="en">
<head>
<meta charset="utf-8">
<title>Tele-Endocrinology Service Brochure</title>
<link href="https://fonts.googleapis.com/css2?family=Oswald:wght@500;600&family=Lato:wght@400;700&display=swap" rel="stylesheet">
<style>
:root{
  --orange:#f7a21b;
  --orange-deep:#ee8f0c;
  --gray:#8a8a8a;
  --gray-dark:#5d5d5d;
  --ink:#2a2a2a;
  --paper:#ffffff;
  --bg:#dcdcdc;
}
*{box-sizing:border-box;margin:0;padding:0}
html,body{width:1200px;height:1200px;overflow:hidden;background:var(--bg);font-family:"Lato",sans-serif;color:var(--ink)}
.canvas{position:relative;width:1200px;height:1200px}
.spread{position:absolute;left:60px;width:1080px;height:540px;display:flex;box-shadow:0 6px 18px rgba(0,0,0,.18)}
.spread--inside{top:30px}
.spread--outside{top:630px}
.panel{position:relative;width:360px;height:540px;background:var(--paper);overflow:hidden}
.panel svg.deco{position:absolute;inset:0;width:100%;height:100%}
.heading{font-family:"Oswald",sans-serif;font-weight:600;text-transform:uppercase;letter-spacing:.3px;color:var(--ink)}
.underline{text-decoration:underline;text-underline-offset:3px}
.ticks{list-style:none;font-size:11.5px;line-height:1.35}
.ticks li{position:relative;padding-left:17px;margin-bottom:2px}
.ticks li::before{content:"";position:absolute;left:0;top:2px;width:9px;height:9px;border:1.3px solid var(--ink)}
.ticks li::after{content:"";position:absolute;left:2px;top:2px;width:7px;height:4px;border-left:2px solid var(--ink);border-bottom:2px solid var(--ink);transform:rotate(-45deg)}
.photo{position:absolute}
.brand-name{position:absolute;font-family:"Lato",sans-serif;font-weight:700;font-size:20px;color:var(--gray-dark)}

/* inside spread */
.how .heading{position:absolute;left:26px;top:120px;font-size:18px}
.how .list-a{position:absolute;left:26px;top:152px;width:315px}
.how .fee{position:absolute;left:0;top:222px;width:360px;background:var(--orange);padding:6px 26px;font-family:"Oswald",sans-serif;font-weight:600;font-style:italic;font-size:16px;color:#fff;line-height:1.15}
.how .list-b{position:absolute;left:26px;top:280px;width:315px}

.commute .top-text{position:absolute;left:0;top:40px;width:360px;text-align:center}
.commute .top-text .heading{color:#fff;font-size:20px}
.commute .top-text p{font-size:12px;font-weight:700;color:var(--ink);margin-top:8px;padding:0 40px;line-height:1.3}
.circles{position:absolute;top:130px;left:40px;width:280px;display:flex;justify-content:space-between}
.circle{width:76px;height:76px;border-radius:50%;border:3px solid #fff}
.partner .heading{position:absolute;left:30px;top:290px;font-size:15px;line-height:1.15;width:300px}
.partner .band{position:absolute;left:30px;top:332px;background:var(--orange);color:var(--ink);font-size:13px;padding:4px 12px;width:230px}
.partner .ticks{position:absolute;left:30px;top:364px;width:310px}

.cover .title{position:absolute;left:30px;top:360px;width:300px;text-align:center}
.cover .title .heading{font-size:28px;line-height:1.1}
.cover .title p{margin-top:14px;color:#fff;font-size:15px;line-height:1.3}
.cover .frame{position:absolute;left:22px;top:345px;width:316px;height:170px;border-left:2px solid var(--gray-dark);border-bottom:2px solid var(--gray-dark)}

/* outside spread */
.front .frame{position:absolute;left:18px;top:18px;width:180px;height:80px;border-left:2px solid var(--gray-dark);border-top:2px solid var(--gray-dark)}
.contact{background:var(--orange);color:#fff;text-align:center}
.contact .heading{color:#fff;font-size:22px;margin-top:40px}
.contact .org{font-size:15px;margin-top:30px}
.contact .icon{display:block;margin:24px auto 6px}
.contact .line{font-size:16px;letter-spacing:.5px;line-height:1.35}
.contact .addr{font-size:16px;line-height:1.3;padding:0 30px}
.helps .heading{position:absolute;left:22px;top:40px;font-size:15px}
.helps .list-c{position:absolute;left:22px;top:66px;width:320px;font-size:10.5px}
.helps .also{position:absolute;left:22px;top:268px;font-size:14px}
.helps .list-d{position:absolute;left:22px;top:292px;width:230px;font-size:10.5px}
</style>
</head>
<body>
<div class="canvas">

  <section class="spread spread--inside">
    <article class="panel how">
      <svg class="deco" viewBox="0 0 360 540" aria-hidden="true">
        <polygon points="0,70 360,70 360,110 0,110" fill="var(--orange)"/>
        <polygon points="200,110 360,0 360,110" fill="var(--gray)"/>
      </svg>
      <h2 class="heading underline">How does it work?</h2>
      <ul class="ticks list-a">
        <li>No Special equipment needed.</li>
        <li>Existing Computers with integrated VideoCam used.</li>
        <li>Endocrinologist bills Insurance directly</li>
        <li>HIPAA Compliant Telehealth Portal ($300 / Month).</li>
      </ul>
      <div class="fee">Covered by Originating Site Facility Fee<br>(about $25 per patient).</div>
      <ul class="ticks list-b">
        <li>Appointment made via Web Portal or by calling our clinic.</li>
        <li>Appts offered within 24 hours both for In-patient and Out-patients</li>
        <li>Patient meets endocrinologist at partner Clinic via telemedicine portal.</li>
        <li>Patient is accompanied by a MA during the appointment</li>
        <li>Patient Notes are faxed electronically to the partner clinic.</li>
      </ul>
      <svg class="photo" style="left:0;top:400px" width="360" height="140" role="img" aria-label="Photo of a gloved hand and a clinician with stethoscope">
        <defs><linearGradient id="g1" x1="0" x2="1"><stop offset="0" stop-color="#e9e6e2"/><stop offset="1" stop-color="#4f86c6"/></linearGradient></defs>
        <polygon points="0,60 360,0 360,140 0,140" fill="url(#g1)"/>
      </svg>
    </article>

    <article class="panel commute">
      <svg class="deco" viewBox="0 0 360 540" aria-hidden="true">
        <polygon points="0,0 360,0 360,230 180,270 0,230" fill="var(--orange)"/>
        <polygon points="0,230 180,270 360,230 360,260 180,300 0,260" fill="var(--gray)"/>
      </svg>
      <div class="top-text">
        <h2 class="heading underline">Save on commute</h2>
        <p>Control Diabetes and Thyroid Disorders Decrease Wait-times for an Endocrinologist Achieve Weight loss</p>
      </div>
      <div class="circles">
        <div class="circle" style="background:#e6c7a8" role="img" aria-label="Photo of a blood sugar test"></div>
        <div class="circle" style="background:#ddd3cc" role="img" aria-label="Photo of a thyroid check"></div>
        <div class="circle" style="background:#d9b79a" role="img" aria-label="Photo of a waist measurement"></div>
      </div>
      <div class="partner">
        <h2 class="heading underline">FQHC, RHC, CAH, Primary Care Physicians can partner with us</h2>
        <div class="band">Advantages to our Partners</div>
        <ul class="ticks">
          <li>Provide Endocrinologist in their own clinic</li>
          <li>Provide Diabetes Education and Nutritionist Services in their clinic</li>
          <li>Improve convenience to patients and reduce wait-time</li>
          <li>No setup cost and low on-going Expenses</li>
          <li>Can be CashFlow Positive</li>
          <li>Use the technology to widen the reach of their own employed physicians.</li>
        </ul>
      </div>
    </article>

    <article class="panel cover">
      <span class="brand-name" style="left:40px;top:32px">Brenmore Care</span>
      <svg class="photo" style="left:0;top:80px" width="360" height="460" role="img" aria-label="Photo of a doctor examining a patient's thyroid">
        <defs><linearGradient id="g2" x1="0" x2="1"><stop offset="0" stop-color="#f0e4e8"/><stop offset="1" stop-color="#d85aa0"/></linearGradient></defs>
        <polygon points="0,0 360,0 360,210 180,230 0,210" fill="url(#g2)"/>
        <polygon points="0,210 180,230 360,130 360,460 0,460" fill="var(--orange)"/>
        <polygon points="230,230 360,130 360,200" fill="var(--gray)"/>
      </svg>
      <div class="frame"></div>
      <div class="title">
        <h1 class="heading">Tele-Endocrinology Service</h1>
        <p>by Southridge Endocrinology<br>and Metabolic Medicine</p>
      </div>
    </article>
  </section>

  <section class="spread spread--outside">
    <article class="panel front">
      <div class="frame"></div>
      <span class="brand-name" style="left:40px;top:48px">Brenmore Care</span>
      <svg class="deco" viewBox="0 0 360 540" aria-hidden="true">
        <rect x="0" y="112" width="360" height="8" fill="var(--orange)"/>
        <polygon points="240,0 360,0 360,60" fill="var(--gray)"/>
      </svg>
      <svg class="photo" style="left:0;top:120px" width="360" height="420" role="img" aria-label="Photo of a smiling doctor in a white coat with stethoscope">
        <defs><linearGradient id="g3" x1="0" x2="1" y1="0" y2="1"><stop offset="0" stop-color="#cfe3ec"/><stop offset="1" stop-color="#f4f7f8"/></linearGradient></defs>
        <rect width="360" height="420" fill="url(#g3)"/>
      </svg>
    </article>

    <article class="panel contact">
      <svg class="deco" viewBox="0 0 360 540" aria-hidden="true">
        <polygon points="0,440 360,400 360,540 0,540" fill="var(--gray)"/>
        <polygon points="0,460 360,430 360,540 0,540" fill="#b7b7b7"/>
      </svg>
      <div style="position:relative">
        <h2 class="heading underline">Contact us</h2>
        <p class="org">Brenmore Care</p>
        <svg class="icon" width="16" height="16" viewBox="0 0 24 24" aria-hidden="true"><path fill="#fff" d="M6.6 10.8a15 15 0 0 0 6.6 6.6l2.2-2.2c.3-.3.7-.4 1-.2 1.1.4 2.3.6 3.6.6.6 0 1 .4 1 1V20c0 .6-.4 1-1 1A17 17 0 0 1 3 4c0-.6.4-1 1-1h3.5c.6 0 1 .4 1 1 0 1.3.2 2.5.6 3.6.1.3 0 .7-.2 1z"/></svg>
        <p class="line">555-210-4848<br>1-800-555-0179</p>
        <svg class="icon" width="18" height="14" viewBox="0 0 24 18" aria-hidden="true"><rect width="24" height="18" rx="2" fill="#fff"/><path d="M1 2l11 8 11-8" stroke="var(--orange)" stroke-width="2" fill="none"/></svg>
        <p class="line">desk@brenmore-care.example</p>
        <svg class="icon" width="14" height="18" viewBox="0 0 24 32" aria-hidden="true"><path fill="#fff" d="M12 0a12 12 0 0 0-12 12c0 9 12 20 12 20s12-11 12-20A12 12 0 0 0 12 0zm0 17a5 5 0 1 1 0-10 5 5 0 0 1 0 10z"/></svg>
        <p class="addr">Southridge Endocrinology and Metabolic Medicine, Riverton</p>
      </div>
    </article>

    <article class="panel helps">
      <svg class="deco" viewBox="0 0 360 540" aria-hidden="true">
        <line x1="200" y1="10" x2="342" y2="10" stroke="var(--gray-dark)" stroke-width="2"/>
        <line x1="342" y1="10" x2="342" y2="34" stroke="var(--gray-dark)" stroke-width="2"/>
        <polygon points="0,390 360,330 360,380 0,420" fill="var(--gray)"/>
      </svg>
      <h2 class="heading underline">Tele-Endocrinology helps in</h2>
      <ul class="ticks list-c">
        <li>Management of type 1 and type 2 diabetes.</li>
        <li>Hypothyroidism, hyperthyroidism, thyroid cancer, thyroid nodules</li>
        <li>Bone disease (Osteoporosis and pagets disease</li>
        <li>Adrenal disorders</li>
        <li>Pituitary tumors</li>
        <li>Polycystic ovarian disease</li>
        <li>Obesity and weight loss</li>
        <li>Calcium disorders (hyperparathyroidism and hypoparathyroidism)</li>
        <li>Male hypogonadism (testosterone replacements)</li>
        <li>Transgender hormone treatment</li>
        <li>Multiple endocrine neoplasia</li>
      </ul>
      <h3 class="heading underline also">Also available</h3>
      <ul class="ticks list-d">
        <li>ADA certified Diabetes Education by Certified Diabetic Educator</li>
        <li>Nutritionist service</li>
      </ul>
      <svg class="photo" style="left:262px;top:270px" width="80" height="60" role="img" aria-label="Photo of a spoon of colourful supplement capsules">
        <ellipse cx="40" cy="30" rx="38" ry="22" fill="#d9b23a"/>
      </svg>
      <svg class="photo" style="left:0;top:390px" width="360" height="150" role="img" aria-label="Photo of a doctor visiting a patient in a hospital bed">
        <defs><linearGradient id="g4" x1="0" x2="1"><stop offset="0" stop-color="#8f7766"/><stop offset="1" stop-color="#c7cde0"/></linearGradient></defs>
        <polygon points="0,30 360,-10 360,150 0,150" fill="url(#g4)"/>
      </svg>
    </article>
  </section>

</div>
</body>
</html>
```